New telco company needs a product page

We need to design two pages - one index and one inner.

We are a new telco company and we have developed our own phone. We will be selling our services and the phone on this site.

The design should be easy to understand and use, following the latest trends in Web design, be clean. It should communicate professionalism and integrity.

The name of our company is VORO which stands for Value Over Rush Often. The design should follow this principle.

Our company logo is attached. I can send it in other colors/sizes - let me know.

Target Market(s)

Aging population (70+), middle-aged with parents and grandparents.

Industry/Entity Type

It Company

Requirements
Must have
• index page, inner page, flat, clean, Pellucor 5 style / ZEB style (quintel.example), easy navigation, fluid layout, CSS, tableless
Should not have
• should not use old fonts, should not use old-style design, should not have animation, should not look like QDX or Bimzo (too busy)

```html
<!DOCTYPE html>
<html lang="en">
<head>
<meta charset="utf-8">
<title>VORO Phone</title>
<link rel="stylesheet" href="https://fonts.googleapis.com/css2?family=Roboto:wght@300;400;500;700&family=Raleway:wght@200;300&display=swap">
<style>
:root{
  --header-grey:#666668;
  --stripe-grey:#7a7a7c;
  --brand-red:#c9444c;
  --deep-red:#b5303a;
  --title-red:#a8212b;
  --footer-grey:#6d6d6f;
  --nav-text:#8a8a8a;
  --white:#ffffff;
  --price-blue:#1b9ad8;
  --screen-light:#dcecf8;
  --screen-mid:#9fcbec;
}
*{box-sizing:border-box;margin:0;padding:0}
html,body{width:1200px;height:1136px;overflow:hidden}
body{position:relative;font-family:"Roboto",Arial,sans-serif;background:var(--brand-red)}
.abs{position:absolute}
.site-header{left:0;top:0;width:1200px;height:120px;background:var(--header-grey)}
.logo{left:122px;top:20px;font-family:"Raleway",sans-serif;font-weight:300;font-size:72px;line-height:1;color:var(--white);letter-spacing:-1px}
.logo-dot{left:254px;top:78px;width:14px;height:14px;border-radius:50%;background:#d8d8d8}
.search-icon{left:892px;top:55px}
.search-field{left:927px;top:54px;width:153px;height:27px;border-radius:14px;background:linear-gradient(#4e4e50,#5c5c5e);border:1px solid #888;box-shadow:inset 0 2px 3px rgba(0,0,0,.4)}
.main-nav{left:313px;top:97px;width:769px;height:48px;background:linear-gradient(#fafafa,#e6e6e6);box-shadow:0 2px 3px rgba(0,0,0,.35);display:flex}
.main-nav a{flex:1;font-size:11px;color:var(--nav-text);text-decoration:none;display:flex;align-items:center;justify-content:center;border-right:1px solid #dcdcdc;position:relative}
.main-nav a:last-child{border-right:0}
.main-nav a.current{background:var(--white);justify-content:flex-start;padding-left:20px}
.main-nav b{color:#666;font-weight:700;margin-left:3px}
.hot-badge{position:absolute;left:86px;top:8px;background:var(--deep-red);color:#fff;font-size:8px;font-weight:700;border-radius:9px;padding:3px 6px;line-height:1}
.hero-frame{left:120px;top:190px;width:295px;height:246px;border:1px solid #e07a80}
.device-large{left:163px;top:195px;width:209px;height:237px;border-radius:8px 8px 0 0;background:linear-gradient(160deg,var(--screen-light),var(--screen-mid));border:7px solid #2c2f36;border-bottom:0}
.device-small{left:447px;top:212px;width:114px;height:224px;border-radius:16px;background:linear-gradient(var(--screen-mid),var(--screen-light));border:6px solid #3f4450;border-top-width:18px;border-bottom-width:18px}
.zoom-box{left:436px;top:226px;width:137px;height:124px;background:rgba(255,255,255,.18);border:1px solid rgba(255,255,255,.5)}
.rays{left:520px;top:241px}
.feature{left:626px;width:173px;height:42px;background:var(--deep-red);color:#fff;font-size:12.5px;font-weight:700;padding-left:15px;display:flex;align-items:center;clip-path:polygon(0 0,94% 0,100% 50%,94% 100%,0 100%)}
.spec-link{left:625px;top:396px;font-size:12px;line-height:14px;color:#eea3a8}
.spec-link u{color:#f6d0d2}
.product-title{left:624px;top:194px;font-family:"Raleway",sans-serif;font-weight:200;font-size:32px;line-height:34px;letter-spacing:-1px;color:var(--white)}
.product-title span{color:var(--title-red)}
.spec-divider{left:822px;top:240px;width:1px;height:190px;background:#d6757b}
.specs{left:848px;top:239px;color:#fff}
.specs dt{font-size:12px;font-weight:700;margin-top:9px}
.specs dt:first-child{margin-top:0}
.specs dd{font-size:9.5px;line-height:14px;margin-top:3px}
.btn{display:flex;align-items:center;justify-content:center;font-weight:700;border-radius:3px}
.btn-learn{left:624px;top:447px;width:177px;height:50px;background:linear-gradient(#d23a44,#a81e28);color:#5a0d14;font-size:17px;box-shadow:0 2px 3px rgba(0,0,0,.3)}
.btn-order{left:823px;top:447px;width:177px;height:50px;background:linear-gradient(#f4f4f4,#c9c9c9);color:#6a6a6a;font-size:17px;box-shadow:0 2px 3px rgba(0,0,0,.3)}
.thumb-panel{left:120px;top:467px;width:441px;height:126px;background:#fff;border-radius:4px}
.thumb{top:491px;width:81px;height:78px;border:1px solid #ccc;background:radial-gradient(#fff 55%,#e6e6e6);display:flex;align-items:center;justify-content:center}
.thumb i{display:block;width:28px;height:54px;border-radius:4px;background:linear-gradient(#222,#444)}
.thumb i.edge{width:5px;background:linear-gradient(90deg,#999,#ddd,#999)}
.thumb i.blue{background:linear-gradient(#2d5fa8,#123063)}
.also-panel{left:120px;top:627px;width:960px;height:233px;background:#fff;border-radius:4px;overflow:hidden}
.also-head{height:40px;background:var(--footer-grey);color:#fff;font-weight:700;font-size:14px;padding:12px 0 0 12px}
.also-item{top:677px;width:120px;margin-left:-60px;text-align:center}
.also-item .handset{display:block;margin:0 auto;width:38px;height:66px;border-radius:7px;background:linear-gradient(#1d1d1d,#444);border:2px solid #777}
.also-item h3{font-family:"Raleway",sans-serif;font-weight:300;font-size:11.5px;line-height:14px;color:#888;margin-top:14px}
.also-item .price{font-size:12px;font-weight:700;color:var(--price-blue);margin-top:4px}
.also-item .btn-small{margin:7px auto 0;width:98px;height:29px;background:linear-gradient(#f0f0f0,#c5c5c5);color:#666;font-size:9px;box-shadow:0 1px 2px rgba(0,0,0,.3)}
.site-footer{left:0;top:898px;width:1200px;height:177px;background:var(--footer-grey)}
.footer-col{top:923px;width:178px;color:#ddd;font-size:12px}
.footer-col h4{font-size:12px;font-weight:700;padding-bottom:13px;border-bottom:1px solid #8a8a8c;margin-bottom:11px}
.footer-col li{list-style:none;line-height:19px}
.footer-col .muted{color:#999}
.legal-bar{left:0;top:1075px;width:1200px;height:61px;background:linear-gradient(#f0f0f0,#d4d4d6)}
.legal-copy{left:120px;top:1099px;font-size:11px;color:#888}
.legal-links{right:120px;top:1099px;font-size:11px;color:#888}
</style>
</head>
<body>
<header class="abs site-header">
  <svg class="abs" style="left:313px;top:0" width="190" height="100" viewBox="0 0 190 100">
    <g fill="var(--stripe-grey)">
      <polygon points="0,0 190,0 184,8 0,8"/>
      <polygon points="0,20 175,20 166,30 0,30"/>
      <polygon points="0,42 160,42 150,52 0,52"/>
      <polygon points="0,64 142,64 132,74 0,74"/>
      <polygon points="0,86 125,86 115,96 0,96"/>
    </g>
  </svg>
  <div class="abs logo">voro</div>
  <div class="abs logo-dot"></div>
  <svg class="abs search-icon" width="24" height="24" viewBox="0 0 24 24"><circle cx="9" cy="9" r="7" fill="none" stroke="#bbb" stroke-width="3"/><line x1="14" y1="14" x2="22" y2="22" stroke="#bbb" stroke-width="4" stroke-linecap="round"/></svg>
  <div class="abs search-field"></div>
</header>
<nav class="abs main-nav">
  <a href="#">Meet<b>voro</b></a>
  <a href="#" class="current">Voro Phone<span class="hot-badge">hot!</span></a>
  <a href="#">Our Products</a>
  <a href="#">News</a>
  <a href="#">Support</a>
  <a href="#">Contact Us</a>
</nav>

<div class="abs hero-frame"></div>
<div class="abs device-large" role="img" aria-label="Voro Phone front view, large"></div>
<svg class="abs rays" width="110" height="140" viewBox="0 0 110 140"><g fill="#b83a43" opacity=".85"><polygon points="0,70 90,10 106,10 106,40"/><polygon points="0,74 106,62 106,92"/><polygon points="0,78 106,114 106,140 90,140"/></g></svg>
<div class="abs device-small" role="img" aria-label="Voro Phone handset"></div>
<div class="abs zoom-box"></div>
<svg class="abs" style="left:496px;top:280px" width="18" height="18" viewBox="0 0 18 18"><circle cx="7" cy="7" r="5" fill="none" stroke="#555" stroke-width="1.5"/><line x1="11" y1="11" x2="16" y2="16" stroke="#555" stroke-width="2"/><line x1="5" y1="7" x2="9" y2="7" stroke="#555"/><line x1="7" y1="5" x2="7" y2="9" stroke="#555"/></svg>

<h1 class="abs product-title"><span>VORO</span> PHONE</h1>
<div class="abs feature" style="top:241px">Super Clear LCD Display</div>
<div class="abs feature" style="top:293px">16GB Internal memory</div>
<div class="abs feature" style="top:345px">Quad Core Processor</div>
<p class="abs spec-link">Click <u>here</u> for Voro Phone's full<br>system specification.</p>
<div class="abs spec-divider"></div>
<dl class="abs specs">
  <dt>Camera</dt><dd>CMOS, 2MP Megapixels Camera Resolution(Front)</dd>
  <dt>OS</dt><dd>Solace OS 4.2.2 (Juniper)</dd>
  <dt>Battery</dt><dd>2,600mAh Standard Battery</dd>
  <dt>Connectors</dt><dd>USB v2.0<br>3.5mm Stereo Earjack<br>MicroSD (up to 64GB)</dd>
</dl>
<a class="abs btn btn-learn">LEARN MORE</a>
<a class="abs btn btn-order">ORDER PRODUCT</a>

<div class="abs thumb-panel"></div>
<div class="abs thumb" style="left:144px"><i role="img" aria-label="Front view thumbnail"></i></div>
<div class="abs thumb" style="left:248px"><i class="edge" role="img" aria-label="Side view thumbnail"></i></div>
<div class="abs thumb" style="left:352px"><i class="blue" role="img" aria-label="Screen on thumbnail"></i></div>
<div class="abs thumb" style="left:456px"><i role="img" aria-label="Back view thumbnail"></i></div>

<section class="abs also-panel"><h2 class="also-head">Also try</h2></section>
<div class="abs also-item" style="left:230px"><span class="handset" role="img" aria-label="Keyboard handset"></span><h3>VORO PRODUCT<br>ONE</h3><p class="price">$300.89</p><a class="btn btn-small">LEARN MORE</a></div>
<div class="abs also-item" style="left:415px"><span class="handset" role="img" aria-label="Touch handset"></span><h3>VORO PRODUCT<br>TWO</h3><p class="price">$300.89</p><a class="btn btn-small">LEARN MORE</a></div>
<div class="abs also-item" style="left:600px"><span class="handset" role="img" aria-label="Slim touch handset"></span><h3>VORO PRODUCT<br>THREE</h3><p class="price">$300.89</p><a class="btn btn-small">LEARN MORE</a></div>
<div class="abs also-item" style="left:785px"><span class="handset" role="img" aria-label="Keyboard handset"></span><h3>VORO PRODUCT<br>FOUR</h3><p class="price">$300.89</p><a class="btn btn-small">LEARN MORE</a></div>
<div class="abs also-item" style="left:970px"><span class="handset" role="img" aria-label="Touch handset"></span><h3>VORO PRODUCT<br>FIVE</h3><p class="price">$300.89</p><a class="btn btn-small">LEARN MORE</a></div>

<footer class="abs site-footer"></footer>
<div class="abs footer-col" style="left:168px"><h4>About&nbsp; Voro</h4><ul><li>Our Company</li><li>Partnerships</li><li>News</li></ul></div>
<div class="abs footer-col" style="left:396px"><h4>Products</h4><ul><li>Smartphones</li><li>Product2</li><li>Product3</li></ul></div>
<div class="abs footer-col" style="left:624px"><h4>Support</h4><ul><li>Call us: 555-0142</li><li>Mail us: <span class="muted">support@voro.example</span></li></ul></div>
<div class="abs footer-col" style="left:852px"><h4>Resources</h4><ul><li>Where to buy?</li><li>Blog</li><li>Product Registration</li></ul></div>

<div class="abs legal-bar"></div>
<p class="abs legal-copy">© 2013 Value Over Rush Often VORO. All rights reserved.</p>
<p class="abs legal-links">Email | Print | Privacy | Sitemap | Terms of Use</p>
</body>
</html>
```